Relaunch of company website (Technical company)

Hi all,

we need a website based on Wordpress who makes the customer curious and excited of all the possibilities we can offer.
Customers are B2B. The layout should be based on the screenshots I added, but refreshed and modernized with some nice gadgets.
All needs to be responsive for the different devices.
We are a technical company. We provide a full range of service from 3D scan, Manufacturing, Prototyping, Bulk production and CAD service.

Later the website needs to have a multi language option.

Home:

1. Logo top left (attached)
2. Menu bar top right
3. Header picture like in the screenshot
4. Than the three small blue pics (CAD - Fertigung - Manufaktur) we want a
hoover-small zoom effect as soon as the mouse hits them.
5. Introduction text of our company
6. Contact Information (Design sample see attachment)
7. At the end "Impressum - Datenschutzerklärung - Haftungsausschluss. Those need to be linked to extra pages where we can add mandatory text (Legal notice, Privacy, Disclaimer)

Leistungen - Our service:

1. See the attachment named our service.
2. First on page a gallery where we can add pictures. If moving the mouse over the picture we want a one line explanation e.g. 3D Scan, Production, Die cast...
no click option at the pictures, just to see.
3. Below that, a side menu (we need to add or remove items by our self if necessary) on the left where we can add our service.
4. If the customer is clicking a service, it needs to be highlighted
5. After clicking a service we want our text to that service appear right of the menu (see attachment sample) and 2 big pictures on top of the menu and text field.

Gallery:

1. Headline pictures for each gallery Category (6-8 at the moment)
2. Mouse over the picture zooms it a little in and adds a text what category it is
e.g. Reverse engineering, Prototyping, Laserscan
3. Clicking on the picture opens the detail gallery to that category. There we need
to add pictures specific to that service.
4. If the customer is clicking on a picture from there, all pictures from that
Category will open in a full screen view mode

Blog:

1. A blog to add news (picture and text). Right now we don´t have the time to feed
it, so we want to deactivate it as long as we cant keep it up to date. Later it
should be part of the website.

Unternehmen:

1. Drop down menu: Our Team - History - Unsere Partner - AGB - Impressum

Our Team:
1. Short description of our employees including picture (see attachment)
2. Contact Information (Design sample see attachment)
3. At the end "Impressum - Datenschutzerklärung - Haftungsausschluss. Those need to be linked to extra pages where we can add mandatory text (Legal notice, Privacy, Disclaimer)

History:
1. Timeline where we can add milestones including date, and pictures of the company (see screenshot)

Unsere Partner:
1. Text field where we can introduce our partners including pictures if necessary.

A blog would be a nice option, social media shortcuts to Instagram-FB but no preview of FB Timeline within the website.

We do have professional text already, that will be added by us. We expect you to use any sample text and pictures for the draft, beside what we supply already.

If you see the need of buying pictures from Quorvane or any other picture company that is OK for us.

What we expect:

A modern, fresh website based on our existing design, changes are fine as long as the whole website design does not change completely to an unicorn thing in pink. Feel free to be creative. New ideas will be discussed, we are open to good ideas. We don´t stick fix to our idea, but we want our customers can see that its still the same company.
Scrolling effects would be a nice gadget if possible.

We have a bad page already...don´t want a second bad one :-)

Our company blue is RBG 106, 206, 224

Greets to all, looking for professional results.

Target Market(s)

B2B, Engineering companys,

Industry/Entity Type

Technical Service

Number of Pages Required

5+ page

Font styles to use
Sans Serif
Other font styles liked:
• verdana

Colors
0455a3
000000
ffffff

Requirements
Must have
• Responsive design, We want to be able to add posts to the Blog, pictures to the categories, and categories by ourself if necessary. (Wordpress)
• Lets say we want to add one more category at „Leistungen-Our Service“ that should be possible for us in the wordpress background.
Nice to have
• Dynamic elements to make the website more alive.
Should not have
• Sliders, Contact form

```html
<!DOCTYPE html>
<html lang="de">
<head>
<meta charset="utf-8">
<title>Vantrel Precision</title>
<link rel="stylesheet" href="https://fonts.googleapis.com/css2?family=Lato:wght@400;700&family=Questrial&display=swap">
<style>
  :root {
    --brand-blue: #0455a3;
    --accent-cyan: #6acee0;
    --ink: #000000;
    --paper: #ffffff;
    --muted: #666a70;
  }
  * { margin: 0; padding: 0; box-sizing: border-box; }
  html, body { width: 934px; height: 1200px; overflow: hidden; }
  body { position: relative; background: var(--paper); font-family: "Lato", sans-serif; color: var(--ink); }

  .site-header { position: absolute; left: 0; top: 0; width: 934px; height: 61px; background: linear-gradient(#f3f3f3, #ffffff 50%, #f0f0f0); }
  .brand { position: absolute; left: 135px; top: 16px; font-family: "Questrial", sans-serif; font-size: 17px; letter-spacing: 0.5px; color: var(--ink); line-height: 1.2; width: 130px; }
  .main-nav { position: absolute; top: 24px; left: 436px; font-size: 10px; letter-spacing: 0.3px; }
  .main-nav a { color: var(--ink); text-decoration: none; position: absolute; white-space: nowrap; }
  .main-nav a.is-active { color: #3fa6e0; }
  .nav-caret { display: inline-block; width: 0; height: 0; border-left: 4px solid var(--ink); border-top: 3px solid transparent; border-bottom: 3px solid transparent; margin-left: 5px; }

  .hero { position: absolute; left: 0; top: 61px; width: 934px; height: 338px;
    background: radial-gradient(circle at 300px 270px, #f3c98a 0, rgba(243,201,138,0) 40px),
                linear-gradient(120deg, #1d2530 0%, #5d6a77 25%, #c6ced6 45%, #8c98a4 65%, #d9dee3 85%, #6f7b87 100%); }
  .hero-title { position: absolute; left: 437px; top: 88px; width: 252px; font-family: "Questrial", sans-serif; color: var(--paper); font-size: 44px; line-height: 1; letter-spacing: 1px; }
  .hero-title .rule { display: block; height: 2px; background: var(--paper); margin: 8px 0 8px; }
  .hero-badge { position: absolute; top: 214px; width: 63px; height: 32px; background: rgba(240,240,240,0.92); }

  .services { position: absolute; left: 0; top: 399px; width: 934px; height: 275px;
    background: linear-gradient(160deg, #2a2d31 0%, #15171a 45%, #050506 100%); }
  .service-card { position: absolute; top: 54px; width: 218px; height: 172px; border: 1px solid #c9d1d6; text-align: center; background: linear-gradient(150deg, rgba(255,255,255,0.04), rgba(0,0,0,0.2)); }
  .service-card.is-accent { border-color: #4fa0b0; }
  .service-card svg { display: block; margin: 36px auto 0; }
  .service-card h2 { font-family: "Questrial", sans-serif; font-variant: small-caps; font-weight: 400; font-size: 24px; margin-top: 5px; color: var(--paper); letter-spacing: 0.5px; }
  .service-card.is-accent h2 { color: var(--accent-cyan); }
  .service-card p { font-family: "Questrial", sans-serif; font-size: 12px; color: var(--paper); letter-spacing: 0.5px; margin-top: 4px; }

  .philosophy { position: absolute; left: 135px; top: 674px; width: 664px; text-align: center; }
  .philosophy h1 { font-family: "Questrial", sans-serif; font-weight: 400; font-size: 22px; line-height: 25px; letter-spacing: 0.5px; margin-top: 29px; }
  .philosophy p { font-size: 7.6px; line-height: 16.7px; color: var(--muted); margin-top: 24px; }
  .philosophy p + p { margin-top: 17px; }

  .contact { position: absolute; left: 0; top: 973px; width: 934px; height: 200px; background: var(--brand-blue); color: var(--paper); }
  .contact-item { position: absolute; top: 29px; width: 200px; text-align: center; }
  .contact-icon { width: 46px; height: 46px; margin: 0 auto; border-radius: 50%; border: 2px solid var(--paper); box-shadow: inset 0 0 0 2px var(--brand-blue), inset 0 0 0 23px var(--paper); display: flex; align-items: center; justify-content: center; }
  .contact-text { margin-top: 10px; font-size: 9px; line-height: 14px; }
  .contact-text.is-large { font-size: 14px; }
  .contact-rule { position: absolute; left: 135px; top: 133px; width: 664px; height: 1px; background: rgba(255,255,255,0.15); }
  .copyright { position: absolute; top: 154px; width: 934px; text-align: center; font-size: 8px; letter-spacing: 0.2px; }
  .legal-links { position: absolute; top: 174px; width: 934px; text-align: center; font-size: 7px; }
  .legal-links a { color: var(--paper); text-decoration: none; }

  .legal-bar { position: absolute; left: 0; top: 1173px; width: 934px; height: 27px; background: var(--ink); }
  .legal-bar a { position: absolute; top: 8px; color: var(--paper); text-decoration: none; font-size: 10px; letter-spacing: 0.3px; transform: translateX(-50%); white-space: nowrap; }
</style>
</head>
<body>

<header class="site-header">
  <div class="brand">Vantrel Precision</div>
  <nav class="main-nav">
    <a class="is-active" href="#" style="left:0">HOME</a>
    <a href="#" style="left:61px">LEISTUNGEN</a>
    <a href="#" style="left:152px">GALERIE</a>
    <a href="#" style="left:225px">BLOG</a>
    <a href="#" style="left:283px">UNTERNEHMEN<span class="nav-caret"></span></a>
  </nav>
</header>

<section class="hero" role="img" aria-label="Laser cutting head sparking over a machined steel plate">
  <div class="hero-title">Vantrel<span class="rule"></span>Precision</div>
  <div class="hero-badge" style="left:438px"></div>
  <div class="hero-badge" style="left:505px"></div>
</section>

<section class="services">
  <article class="service-card" style="left:135px">
    <svg width="70" height="48" viewBox="0 0 70 48" fill="none" stroke="#fff" stroke-width="3">
      <rect x="13" y="2" width="44" height="44"/>
    </svg>
    <h2>Cad service</h2>
    <p>3D SCAN - REVERSE ENGINEERING</p>
  </article>
  <article class="service-card is-accent" style="left:358px">
    <svg width="70" height="48" viewBox="0 0 70 48" fill="none" stroke="#6acee0">
      <circle cx="22" cy="30" r="12" stroke-width="8" stroke-dasharray="4 3"/>
      <circle cx="22" cy="30" r="7" stroke-width="5"/>
      <circle cx="50" cy="14" r="9" stroke-width="6" stroke-dasharray="3 2.5"/>
      <circle cx="50" cy="14" r="5" stroke-width="4"/>
    </svg>
    <h2>Fertigung</h2>
    <p style="margin-top:8px">NATIONAL - INTERNATIONAL</p>
  </article>
  <article class="service-card is-accent" style="left:582px">
    <svg width="60" height="48" viewBox="0 0 60 48" fill="none" stroke="#6acee0" stroke-width="3.5" stroke-linejoin="round">
      <path d="M2 14 L14 2 L58 2 L58 34 L46 46 L2 46 Z"/>
      <path d="M2 14 L46 14 L58 2 M46 14 L46 46"/>
    </svg>
    <h2>Manufaktur</h2>
    <p>MODELLBAU - PROTOTYPEN</p>
  </article>
</section>

<section class="philosophy">
  <h1>UNSERE PHILOSOPHIE IST ES,<br>SYNERGIEN ZU NUTZEN</h1>
  <p>Nunc ac magna urna. Proin lacinia tellus at erat maximus, quis pellentesque magna sodales. Sed nec vehicula magna, non pretium leo. Sed ac sem in lacus pulvinar luctus. Curabitur risus nisi, efficitur sit amet efficitur eget, viverra sit amet sapien. Vestibulum porttitor ligula dignissim risus facilisis, in hendrerit eros imperdiet. Nullam ut iaculis arcu, volutpat ullamcorper turpis. Fusce eu bibendum erat. Quisque porta ullamcorper gravida. Nullam augue urna, egestas a elit sit amet, varius rutrum lectus. Pellentesque est lorem, tincidunt a leo at, mollis mollis lectus. Nam varius purus sit amet orci tempor varius. Sed vel mollis est. Fusce tincidunt purus non maximus maximus. Donec elementum libero metus, ut sodales est mattis ac.</p>
  <p>Morbi ut ornare quam. Aenean volutpat risus eu leo eleifend, vel commodo neque sollicitudin. Aliquam varius placerat nibh, sit amet lobortis massa interdum in. Maecenas elementum velit metus. Donec vitae leo eu tortor sagittis sollicitudin. Pellentesque nec leo eu odio lacinia viverra. Phasellus sed ligula in dolor ultricies fringilla ut a elit. Maecenas id laoreet quam. Nullam luctus, nisl a vulputate fringilla, sapien ex consequat enim, eget interdum turpis mauris at massa. In consectetur lacinia sapien sit amet faucibus. Donec pretium odio nulla, non pretium enim elementum sit amet. Etiam ut suscipit leo, nec commodo leo. Sed porta a dolor at blandit. Nullam nisi dolor, convallis sit amet condimentum vestibulum, viverra et libero. Quisque vitae lectus ex. Mauris imperdiet justo dui, non pellentesque enim pharetra et.</p>
</section>

<footer class="contact">
  <div class="contact-item" style="left:174px">
    <div class="contact-icon">
      <svg width="12" height="20" viewBox="0 0 12 20"><rect x="1" y="1" width="10" height="18" rx="2" fill="none" stroke="#0455a3" stroke-width="2"/><rect x="3" y="4" width="6" height="9" fill="#0455a3"/><circle cx="6" cy="16" r="1.2" fill="#0455a3"/></svg>
    </div>
    <div class="contact-text is-large">+(400) 555 014 238</div>
  </div>
  <div class="contact-item" style="left:365px">
    <div class="contact-icon">
      <svg width="12" height="18" viewBox="0 0 12 18"><path d="M6 0 C2.7 0 0 2.6 0 6 C0 10 6 18 6 18 C6 18 12 10 12 6 C12 2.6 9.3 0 6 0 Z" fill="#0455a3"/><circle cx="6" cy="6" r="2.3" fill="#fff"/></svg>
    </div>
    <div class="contact-text">48 Elmbrook Lane, ed porta a dolor,<br>ZX 40127, Nordland</div>
  </div>
  <div class="contact-item" style="left:561px">
    <div class="contact-icon">
      <svg width="18" height="14" viewBox="0 0 18 14"><rect x="0" y="0" width="18" height="14" rx="2" fill="#0455a3"/><path d="M1 2 L9 8 L17 2" fill="none" stroke="#fff" stroke-width="1.6"/></svg>
    </div>
    <div class="contact-text">info@vantrelprecision.com</div>
  </div>
  <div class="contact-rule"></div>
  <div class="copyright">COPYRIGHT © 2018 &nbsp;VANTREL PRECISION, &nbsp;ALL RIGHTS RESERVED</div>
  <div class="legal-links"><a href="#">LEGAL NOTICE</a> | <a href="#">PRIVACY</a> | <a href="#">DISCLAIMER</a></div>
</footer>

<nav class="legal-bar">
  <a href="#" style="left:270px">IMPRESSUM</a>
  <a href="#" style="left:467px">DATENSCHUTZERKLÄRUNG</a>
  <a href="#" style="left:668px">HAFTUNGSAUSSCHLUSS</a>
</nav>

</body>
</html>
```